Design a New Business Card for Our Company

We are looking for fresh, unique, and a modern business card that reflects our roots as digital marketing agency focused on SEM.

Industry/Entity Type

Marketing

Contact Information for Business Card

looking for very unique out of the box designs. clean and modern that compliments our logo

Requirements
Must have
• colors should match our logo
• Front should have name, address, email, and phone/fax of the person, phone/fax are the same number
• back should have our url

```html
<!DOCTYPE html>
<html lang="en">
<head>
<meta charset="utf-8">
<title>Northfield Digital – Business Card</title>
<link rel="stylesheet" href="https://fonts.googleapis.com/css2?family=Open+Sans:wght@400;600&display=swap">
<style>
  :root {
    --stage: #3b3b3b;
    --card-white: #ffffff;
    --card-grey: #b3b3b3;
    --band-grey: #a9a9a9;
    --brand-blue: #5b93d3;
    --name-grey: #a3a3a3;
    --text-dark: #555555;
    --icon-grey: #9c9c9c;
    --divider: #c8c8c8;
  }
  * { box-sizing: border-box; margin: 0; padding: 0; }
  html, body {
    width: 1105px;
    height: 1200px;
    overflow: hidden;
    background: var(--stage);
    font-family: "Open Sans", Arial, sans-serif;
  }
  .card {
    position: absolute;
    left: 196px;
    width: 720px;
    height: 410px;
    overflow: hidden;
  }
  .card--front { top: 146px; background: var(--card-white); }
  .card--back  { top: 602px; background: var(--card-grey); }

  /* Front */
  .brand {
    position: absolute;
    left: 66px;
    top: 170px;
    display: flex;
    align-items: center;
    gap: 12px;
  }
  .brand__dot {
    width: 24px;
    height: 24px;
    border-radius: 50%;
    background: var(--brand-blue);
  }
  .brand__name {
    font-size: 30px;
    font-weight: 600;
    color: var(--name-grey);
    letter-spacing: -0.3px;
  }
  .divider {
    position: absolute;
    left: 378px;
    top: 75px;
    width: 1px;
    height: 248px;
    background: var(--divider);
  }
  .contact {
    position: absolute;
    left: 409px;
    top: 92px;
    color: var(--text-dark);
  }
  .contact__name {
    font-size: 25px;
    font-weight: 600;
    color: var(--name-grey);
    line-height: 32px;
  }
  .contact__title {
    font-size: 19px;
    color: var(--brand-blue);
    line-height: 26px;
    margin-bottom: 14px;
  }
  .contact__address {
    font-size: 19px;
    line-height: 28px;
    margin-bottom: 12px;
  }
  .contact__list { list-style: none; }
  .contact__item {
    display: flex;
    align-items: center;
    font-size: 19px;
    line-height: 28px;
  }
  .contact__icon {
    width: 18px;
    height: 18px;
    margin: 0 10px 0 8px;
    fill: var(--icon-grey);
  }
  .front-band {
    position: absolute;
    left: 0;
    bottom: 0;
    width: 100%;
    height: 34px;
    background: var(--band-grey);
    border-top: 3px solid var(--brand-blue);
    box-shadow: inset 0 2px 0 var(--card-white);
  }

  /* Back */
  .back-brand {
    position: absolute;
    left: 0;
    top: 95px;
    width: 100%;
    display: flex;
    flex-direction: column;
    align-items: center;
    gap: 18px;
  }
  .back-brand__dot {
    width: 80px;
    height: 80px;
    border-radius: 50%;
    background: var(--card-white);
  }
  .back-brand__name {
    font-size: 32px;
    font-weight: 600;
    color: var(--card-white);
  }
  .back-url {
    position: absolute;
    left: 0;
    top: 346px;
    width: 100%;
    text-align: center;
    font-size: 18px;
    letter-spacing: 4px;
    color: var(--card-white);
  }
</style>
</head>
<body>
  <section class="card card--front">
    <div class="brand">
      <span class="brand__dot"></span>
      <span class="brand__name">Northfield Digital</span>
    </div>
    <div class="divider"></div>
    <div class="contact">
      <p class="contact__name">Daniel Reyes</p>
      <p class="contact__title">CEO/Founder</p>
      <p class="contact__address">2140 Harbor View Road<br>Fairbanks, Alaska 99712</p>
      <ul class="contact__list">
        <li class="contact__item">
          <svg class="contact__icon" viewBox="0 0 24 24" aria-hidden="true"><path d="M6.6 10.8a15.2 15.2 0 0 0 6.6 6.6l2.2-2.2a1 1 0 0 1 1-.25 11.4 11.4 0 0 0 3.6.57 1 1 0 0 1 1 1V20a1 1 0 0 1-1 1A17 17 0 0 1 3 4a1 1 0 0 1 1-1h3.5a1 1 0 0 1 1 1c0 1.25.2 2.45.57 3.6a1 1 0 0 1-.25 1z"/></svg>
          555 318 2046
        </li>
        <li class="contact__item">
          <svg class="contact__icon" viewBox="0 0 24 24" aria-hidden="true"><path d="M6 2h10v5H6z M3 8h18a1 1 0 0 1 1 1v9a1 1 0 0 1-1 1H3a1 1 0 0 1-1-1V9a1 1 0 0 1 1-1z M6 14h12v8H6z" /></svg>
          555 318 2047
        </li>
        <li class="contact__item">
          <svg class="contact__icon" viewBox="0 0 24 24" aria-hidden="true"><path d="M2 5h20v14H2z M3 6l9 7 9-7" stroke="#ffffff" stroke-width="1.5"/></svg>
          dan@nfdigital.com
        </li>
      </ul>
    </div>
    <div class="front-band"></div>
  </section>

  <section class="card card--back">
    <div class="back-brand">
      <span class="back-brand__dot"></span>
      <span class="back-brand__name">Northfield Digital</span>
    </div>
    <p class="back-url">www.nfdigital.com</p>
  </section>
</body>
</html>
```